upgrade business card

I have had a nice business card/loyalty card for my business, I have notice that I need a personal business card to hand to certain people that I need to contact me directly or for networking porpouses.

I also would need to take the same loyalty card\business card I have been using and add the manager's name, leave everything else the same!

I will upload the one I am currently using so you guys can add the manager's name that would be the one that is black background with white letters then I will upload one that has a white background so you can work around it to desing my personal one.

for my personal one I would like to have the shop's logo on one side( white background, black logo, reasonable big as its only the logo)

on the other side I would like you to use the template I will upload, put my name ( Tomás Ilvarre) where it says loyalty card, put the shop logo in black on the top right corner(just the logo without the cloud shaped thing) and then under where the phone number is +353 (87) 402 9315 also included a whatsapp logo.

for email Tomas@quellbrook-mail.ie

for social media delete the fb logo and just put the instagram one and my instagram would be @Tomas_428, feel free to do something different that you guys would consider better

```html
<!DOCTYPE html>
<html lang="en">
<head>
<meta charset="UTF-8">
<title>Talven – Personal Business Card</title>
<link href="https://fonts.googleapis.com/css2?family=Poppins:wght@400;600&display=swap" rel="stylesheet">
<style>
  :root {
    --backdrop: #3b3e45;
    --card-white: #ffffff;
    --card-black: #231f20;
    --ink-white: #ffffff;
    --ink-grey: #8a8a8a;
    --shadow: rgba(0, 0, 0, 0.35);
  }
  * { margin: 0; padding: 0; box-sizing: border-box; }
  html, body {
    width: 1200px;
    height: 855px;
    overflow: hidden;
    background: var(--backdrop);
    font-family: "Poppins", sans-serif;
  }
  .card {
    position: absolute;
    left: 282px;
    width: 636px;
    height: 369px;
    box-shadow: 0 8px 22px var(--shadow);
  }
  .card--front {
    top: 33px;
    background: var(--card-white);
  }
  .brand-band {
    position: absolute;
    left: 0;
    top: 139px;
    width: 100%;
    height: 90px;
    background: var(--card-black);
    display: flex;
    align-items: center;
    justify-content: center;
  }
  .brand-lockup {
    display: flex;
    flex-direction: column;
    align-items: flex-end;
    margin-left: 36px;
  }
  .brand-name {
    color: var(--ink-white);
    font-weight: 600;
    font-size: 62px;
    line-height: 1;
    letter-spacing: 1px;
  }
  .brand-web {
    color: var(--ink-white);
    font-weight: 600;
    font-size: 20px;
    line-height: 1;
    letter-spacing: 2px;
    margin-top: 1px;
  }
  .card--back {
    top: 465px;
    background: var(--card-black);
  }
  .person {
    position: absolute;
    left: 51px;
    top: 153px;
  }
  .person-name {
    color: var(--ink-white);
    font-weight: 600;
    font-size: 28px;
    line-height: 1.1;
    letter-spacing: 0.5px;
  }
  .person-role {
    color: var(--ink-grey);
    font-weight: 400;
    font-size: 14px;
    letter-spacing: 0.8px;
    margin-top: 1px;
  }
  .divider {
    position: absolute;
    left: 318px;
    top: 125px;
    width: 2px;
    height: 108px;
    background: var(--ink-white);
  }
  .contact-list {
    position: absolute;
    left: 358px;
    top: 127px;
    list-style: none;
  }
  .contact-item {
    display: flex;
    align-items: center;
    height: 30px;
    color: var(--ink-white);
    font-size: 15px;
    font-weight: 400;
  }
  .contact-icon {
    width: 16px;
    height: 16px;
    margin-right: 16px;
    fill: var(--ink-white);
    flex-shrink: 0;
  }
  .contact-marker {
    width: 12px;
    height: 12px;
    margin: 0 18px 0 2px;
    background: var(--ink-white);
    flex-shrink: 0;
  }
</style>
</head>
<body>
  <section class="card card--front">
    <div class="brand-band">
      <div class="brand-lockup">
        <span class="brand-name">TALVEN</span>
        <span class="brand-web">talven.ie</span>
      </div>
    </div>
  </section>

  <section class="card card--back">
    <div class="person">
      <h1 class="person-name">TOMÁS ILVARRE</h1>
      <p class="person-role">MANAGER</p>
    </div>
    <div class="divider"></div>
    <ul class="contact-list">
      <li class="contact-item">
        <svg class="contact-icon" viewBox="0 0 24 24" aria-hidden="true"><path d="M6.6 10.8a15.1 15.1 0 0 0 6.6 6.6l2.2-2.2c.3-.3.7-.4 1-.2 1.1.4 2.3.6 3.6.6.6 0 1 .4 1 1V20c0 .6-.4 1-1 1A17 17 0 0 1 3 4c0-.6.4-1 1-1h3.5c.6 0 1 .4 1 1 0 1.3.2 2.5.6 3.6.1.3 0 .7-.2 1z"/></svg>
        <span>+353 (87) 402 9315</span>
      </li>
      <li class="contact-item">
        <svg class="contact-icon" viewBox="0 0 24 24" aria-hidden="true"><path d="M2 5h20v14H2z"/><path d="M3 6l9 6.3L21 6" fill="none" stroke="var(--card-black)" stroke-width="1.8"/></svg>
        <span>Tomas@quellbrook-mail.ie</span>
      </li>
      <li class="contact-item">
        <span class="contact-marker" aria-hidden="true"></span>
        <span>@Tomas_428</span>
      </li>
    </ul>
  </section>
</body>
</html>
```